Graffiti removal company needs cool flyer

Beacon Rinse & Spray is a pressure washing company based in Alberta, Canada - we offer general power washing and graffiti removal services for residential & commercial properties. . We would like an edgy/cool 2 sided flyer created to hand out to business / possible door hanger style with specific focus on graffiti removal but also touching on the power washing we can provide. The flyer should have the added pictures (use some before & afters) & wording attached. The picture from Harlow Dome should be used as its a prominent sports arena. There should be some graffiti fonts used to convey the titles/ steps/headings but the look should be clean.
Contact info to appear on flyer
Company logo
Ph 780-555-0143
derek@beaconrinse.ca
www.beaconrinseandspray.ca

```html
<!DOCTYPE html>
<html lang="en">
<head>
<meta charset="utf-8">
<title>Beacon Rinse & Spray – Graffiti Removal Door Hanger</title>
<link href="https://fonts.googleapis.com/css2?family=Montserrat:wght@400;600;700;800;900&family=Sedgwick+Ave+Display&display=swap" rel="stylesheet">
<style>
:root{
  --navy:#16295a;
  --navy-deep:#0f1d42;
  --blue:#1f5fa8;
  --sky:#d9e4f2;
  --ink:#1c2230;
  --grey-text:#4a5263;
  --white:#ffffff;
  --stage:#a9a9a9;
}
*{box-sizing:border-box;margin:0;padding:0}
html,body{width:1200px;height:2836px;overflow:hidden}
body{background:var(--stage);font-family:"Montserrat",Arial,sans-serif;color:var(--ink);position:relative}
.hanger{position:absolute;width:420px;height:1320px;background:var(--white);overflow:hidden;border-radius:6px;box-shadow:0 4px 14px rgba(0,0,0,.18)}
.hanger .hole{position:absolute;top:62px;width:92px;height:92px;border-radius:50%;background:var(--stage);z-index:9}
.abs{position:absolute}
.photo{position:absolute}
.graffiti{font-family:"Sedgwick Ave Display",cursive;color:var(--navy);line-height:.9;letter-spacing:1px}
.brand{position:absolute;display:flex;align-items:center;gap:8px}
.brand .mark{width:22px;height:22px;background:var(--navy)}
.brand .name{font-weight:800;font-size:14px;color:var(--navy);line-height:1.05;text-transform:uppercase}
.label{position:absolute;background:var(--navy);color:var(--white);font-weight:800;font-size:13px;letter-spacing:1px;text-align:center;padding:5px 0}
.feature-head{position:absolute;display:flex;align-items:center;gap:8px;font-weight:900;font-size:17px;color:var(--navy);letter-spacing:.5px}
.feature-head .icon{width:28px;height:28px;border-radius:50%;background:var(--blue);display:flex;align-items:center;justify-content:center}
.copy{position:absolute;font-size:11.5px;line-height:1.45;color:var(--grey-text)}
.band{position:absolute;background:var(--navy);color:var(--white)}
.contact-phone{position:absolute;display:flex;align-items:center;gap:8px;font-weight:900;font-size:24px}
.contact-lines{position:absolute;font-size:10.5px;line-height:1.7;font-weight:600}
/* front */
.front .hole{left:144px}
.front .hero{left:0;top:0;width:420px;height:400px;background:linear-gradient(160deg,#6d7f95 0%,#b7bcc3 45%,#8a8f96 100%)}
.front .hero-cut{left:0;top:300px;width:420px;height:110px}
.front .brand{left:210px;top:316px}
.front .title{left:22px;top:396px;font-size:72px}
.front .before{left:18px;top:590px;width:180px;height:160px;background:linear-gradient(135deg,#9b5a3c,#c98a62 50%,#7d4a35)}
.front .after{left:18px;top:800px;width:180px;height:150px;background:linear-gradient(135deg,#b9724a,#d9a27a 55%,#a36646)}
.front .why{left:0;top:1000px;width:420px;height:180px;padding:20px 22px}
.front .why h3{font-weight:900;font-size:14px;letter-spacing:.4px;margin-bottom:10px}
.front .why p{font-size:11.5px;line-height:1.5;color:#d5ddec}
.front .contact-phone{left:22px;top:1232px;color:var(--navy)}
.front .contact-lines{left:240px;top:1228px;color:var(--grey-text)}
/* back */
.back .hole{left:176px}
.back .arena{left:0;top:0;width:420px;height:560px;background:linear-gradient(180deg,#c9d4e0 0%,#e6e9ec 40%,#8e969f 100%)}
.back .panel{left:0;top:400px;width:420px;height:420px}
.back .easy{left:150px;top:430px;text-align:center;width:180px}
.back .easy .small{font-size:40px;display:block}
.back .easy .big{font-size:46px;display:block}
.back .steps{left:20px;top:525px;width:380px;height:120px}
.back .step-text{position:absolute;font-size:9.5px;font-weight:600;color:var(--grey-text);text-align:center;width:84px}
.back .truck{left:14px;top:650px;width:150px;height:100px;background:linear-gradient(135deg,#dfe3e8,#9aa3ad)}
.back .info-box{left:170px;top:650px;width:110px;height:150px;background:var(--sky);padding:10px;font-size:9.5px;line-height:1.45;color:var(--grey-text);border-radius:4px}
.back .since{left:290px;top:650px;width:116px;height:150px;background:var(--navy);color:var(--white);padding:14px 10px;font-weight:800;font-size:13px;line-height:1.3;text-align:center;border-radius:4px}
.back .since strong{display:block;font-size:18px;margin-top:10px;color:#9fc2ec}
.back .study{left:22px;top:845px;width:376px}
.back .before{left:18px;top:925px;width:184px;height:150px;background:linear-gradient(135deg,#8c7f73,#c2b4a2 50%,#6e645b)}
.back .after{left:218px;top:925px;width:184px;height:150px;background:linear-gradient(135deg,#a69b90,#d8cfc4 55%,#938a80)}
.back .brand{left:20px;top:1118px}
.back .call{left:210px;top:1112px;width:196px;font-size:10.5px;line-height:1.4;color:var(--grey-text)}
.back .call strong{color:var(--navy);font-weight:800}
.back .footer{left:0;top:1190px;width:420px;height:130px}
.back .contact-phone{left:22px;top:1240px;color:var(--white)}
.back .contact-lines{left:240px;top:1236px;color:var(--white)}
</style>
</head>
<body>

<!-- Row 1 -->
<div class="hanger front" style="left:170px;top:40px">
  <div class="hole"></div>
  <div class="photo hero" role="img" aria-label="Technician in blue coveralls pressure washing graffiti off a brick wall"></div>
  <svg class="abs hero-cut" viewBox="0 0 420 110" preserveAspectRatio="none"><path d="M0 100 C120 90 170 20 260 10 C320 4 380 8 420 0 V110 H0Z" fill="#fff"/><path d="M0 96 C120 86 170 16 260 6 C320 0 380 4 420 -4" stroke="#1f5fa8" stroke-width="5" fill="none"/></svg>
  <div class="brand"><span class="mark"></span><span class="name">Beacon Rinse<br>&amp; Spray</span></div>
  <div class="abs graffiti title">Graffiti<br>Removal</div>
  <div class="photo before" role="img" aria-label="Brick wall covered in graffiti before cleaning"></div>
  <div class="label" style="left:18px;top:750px;width:180px">BEFORE</div>
  <div class="photo after" role="img" aria-label="Same brick wall clean after graffiti removal"></div>
  <div class="label" style="left:18px;top:950px;width:180px">AFTER</div>
  <div class="feature-head" style="left:212px;top:590px"><span class="icon"><svg width="14" height="14" viewBox="0 0 14 14"><path d="M2 7l3 3 7-7" stroke="#fff" stroke-width="2.4" fill="none"/></svg></span>TRUSTED</div>
  <p class="copy" style="left:212px;top:628px;width:192px">Beacon Rinse &amp; Spray provides graffiti removal services to businesses and homes across Alberta with safe, proven methods.</p>
  <div class="feature-head" style="left:212px;top:740px"><span class="icon"><svg width="14" height="14" viewBox="0 0 14 14"><circle cx="7" cy="7" r="5.5" stroke="#fff" stroke-width="1.8" fill="none"/><path d="M7 3.5V7l2.4 1.6" stroke="#fff" stroke-width="1.8" fill="none"/></svg></span>QUICK RESPONSE</div>
  <p class="copy" style="left:212px;top:778px;width:192px">We answer calls fast and arrange a visit within days so tags never stay up long.</p>
  <div class="band" style="left:212px;top:880px;width:190px;padding:6px 10px;font-weight:900;font-size:14px">ABOUT US</div>
  <p class="copy" style="left:212px;top:914px;width:192px">Serving Alberta since 2011, our crew handles graffiti removal and pressure washing for every type of property.</p>
  <div class="band why"><h3>WHY IS IT IMPORTANT TO REMOVE GRAFFITI QUICKLY?</h3><p>Graffiti left in place invites more tagging. Quick removal keeps your building clean, protects surfaces and shows your neighbourhood the property is cared for.</p></div>
  <div class="contact-phone"><svg width="24" height="24" viewBox="0 0 24 24"><path d="M6.6 10.8a15 15 0 006.6 6.6l2.2-2.2c.3-.3.7-.4 1-.2 1.1.4 2.3.6 3.6.6.6 0 1 .4 1 1V20c0 .6-.4 1-1 1A17 17 0 013 4c0-.6.4-1 1-1h3.5c.6 0 1 .4 1 1 0 1.3.2 2.5.6 3.6.1.3 0 .7-.2 1z" fill="#16295a"/></svg>780-555-0143</div>
  <div class="contact-lines">derek@beaconrinse.ca<br>www.beaconrinseandspray.ca</div>
</div>

<div class="hanger back" style="left:610px;top:40px">
  <div class="hole"></div>
  <div class="photo arena" role="img" aria-label="Harlow Dome sports arena exterior"></div>
  <svg class="abs panel" viewBox="0 0 420 420" preserveAspectRatio="none"><path d="M0 60 C90 20 150 0 210 0 C280 0 340 30 420 60 V420 H0Z" fill="#fff"/></svg>
  <div class="abs graffiti easy"><span class="small">Easy as</span><span class="big">1, 2, 3</span></div>
  <svg class="abs steps" viewBox="0 0 380 120">
    <circle cx="48" cy="34" r="26" fill="#16295a"/><circle cx="190" cy="34" r="26" fill="#16295a"/><circle cx="332" cy="34" r="26" fill="#16295a"/>
    <text x="48" y="40" fill="#fff" font-family="Montserrat,Arial,sans-serif" font-weight="900" font-size="18" text-anchor="middle">01</text>
    <text x="190" y="40" fill="#fff" font-family="Montserrat,Arial,sans-serif" font-weight="900" font-size="18" text-anchor="middle">02</text>
    <text x="332" y="40" fill="#fff" font-family="Montserrat,Arial,sans-serif" font-weight="900" font-size="18" text-anchor="middle">03</text>
    <path d="M80 34H150M222 34H292" stroke="#1f5fa8" stroke-width="3"/><path d="M150 28l8 6-8 6zM292 28l8 6-8 6z" fill="#1f5fa8"/>
  </svg>
  <div class="step-text" style="left:26px;top:590px">Call us for a free quote</div>
  <div class="step-text" style="left:168px;top:590px">We assess the surface and plan</div>
  <div class="step-text" style="left:310px;top:590px">Graffiti gone, property restored</div>
  <div class="photo truck" role="img" aria-label="White service truck with pressure washing equipment"></div>
  <div class="abs info-box">Beacon Rinse &amp; Spray removes graffiti and washes walls, lots and entrances across the region.</div>
  <div class="abs since">WASHING &amp; STEAMING SERVICES<strong>SINCE 2011</strong></div>
  <p class="copy study">Studies have shown that fast removal is the best way to prevent repeat graffiti and keep a property looking its best.</p>
  <div class="photo before" role="img" aria-label="Concrete wall with graffiti before cleaning"></div>
  <div class="label" style="left:18px;top:1075px;width:184px">BEFORE</div>
  <div class="photo after" role="img" aria-label="Concrete wall clean after graffiti removal"></div>
  <div class="label" style="left:218px;top:1075px;width:184px">AFTER</div>
  <div class="brand"><span class="mark"></span><span class="name">Beacon Rinse<br>&amp; Spray</span></div>
  <p class="abs call">No matter what's seen on your property, we clean it up. <strong>Call Beacon Rinse &amp; Spray.</strong></p>
  <svg class="abs footer" viewBox="0 0 420 130" preserveAspectRatio="none"><path d="M0 20 C140 0 280 0 420 20 V130 H0Z" fill="#16295a"/></svg>
  <div class="contact-phone"><svg width="24" height="24" viewBox="0 0 24 24"><path d="M6.6 10.8a15 15 0 006.6 6.6l2.2-2.2c.3-.3.7-.4 1-.2 1.1.4 2.3.6 3.6.6.6 0 1 .4 1 1V20c0 .6-.4 1-1 1A17 17 0 013 4c0-.6.4-1 1-1h3.5c.6 0 1 .4 1 1 0 1.3.2 2.5.6 3.6.1.3 0 .7-.2 1z" fill="#fff"/></svg>780-555-0143</div>
  <div class="contact-lines">derek@beaconrinse.ca<br>www.beaconrinseandspray.ca</div>
</div>

<!-- Row 2 -->
<div class="hanger front" style="left:170px;top:1470px">
  <div class="hole"></div>
  <div class="photo hero" role="img" aria-label="Technician in blue coveralls pressure washing graffiti off a brick wall"></div>
  <svg class="abs hero-cut" viewBox="0 0 420 110" preserveAspectRatio="none"><path d="M0 100 C120 90 170 20 260 10 C320 4 380 8 420 0 V110 H0Z" fill="#fff"/><path d="M0 96 C120 86 170 16 260 6 C320 0 380 4 420 -4" stroke="#1f5fa8" stroke-width="5" fill="none"/></svg>
  <div class="brand"><span class="mark"></span><span class="name">Beacon Rinse<br>&amp; Spray</span></div>
  <div class="abs graffiti title">Graffiti<br>Removal</div>
  <div class="photo before" role="img" aria-label="Brick wall covered in graffiti before cleaning"></div>
  <div class="label" style="left:18px;top:750px;width:180px">BEFORE</div>
  <div class="photo after" role="img" aria-label="Same brick wall clean after graffiti removal"></div>
  <div class="label" style="left:18px;top:950px;width:180px">AFTER</div>
  <div class="feature-head" style="left:212px;top:590px"><span class="icon"><svg width="14" height="14" viewBox="0 0 14 14"><path d="M2 7l3 3 7-7" stroke="#fff" stroke-width="2.4" fill="none"/></svg></span>TRUSTED</div>
  <p class="copy" style="left:212px;top:628px;width:192px">Beacon Rinse &amp; Spray provides graffiti removal services to businesses and homes across Alberta with safe, proven methods.</p>
  <div class="feature-head" style="left:212px;top:740px"><span class="icon"><svg width="14" height="14" viewBox="0 0 14 14"><circle cx="7" cy="7" r="5.5" stroke="#fff" stroke-width="1.8" fill="none"/><path d="M7 3.5V7l2.4 1.6" stroke="#fff" stroke-width="1.8" fill="none"/></svg></span>QUICK RESPONSE</div>
  <p class="copy" style="left:212px;top:778px;width:192px">We answer calls fast and arrange a visit within days so tags never stay up long.</p>
  <div class="band" style="left:212px;top:880px;width:190px;padding:6px 10px;font-weight:900;font-size:14px">ABOUT US</div>
  <p class="copy" style="left:212px;top:914px;width:192px">Serving Alberta since 2011, our crew handles graffiti removal and pressure washing for every type of property.</p>
  <div class="band why"><h3>WHY IS IT IMPORTANT TO REMOVE GRAFFITI QUICKLY?</h3><p>Graffiti left in place invites more tagging. Quick removal keeps your building clean, protects surfaces and shows your neighbourhood the property is cared for.</p></div>
  <div class="contact-phone"><svg width="24" height="24" viewBox="0 0 24 24"><path d="M6.6 10.8a15 15 0 006.6 6.6l2.2-2.2c.3-.3.7-.4 1-.2 1.1.4 2.3.6 3.6.6.6 0 1 .4 1 1V20c0 .6-.4 1-1 1A17 17 0 013 4c0-.6.4-1 1-1h3.5c.6 0 1 .4 1 1 0 1.3.2 2.5.6 3.6.1.3 0 .7-.2 1z" fill="#16295a"/></svg>780-555-0143</div>
  <div class="contact-lines">derek@beaconrinse.ca<br>www.beaconrinseandspray.ca</div>
</div>

<div class="hanger back" style="left:610px;top:1470px">
  <div class="hole"></div>
  <div class="photo arena" role="img" aria-label="Harlow Dome sports arena exterior"></div>
  <svg class="abs panel" viewBox="0 0 420 420" preserveAspectRatio="none"><path d="M0 60 C90 20 150 0 210 0 C280 0 340 30 420 60 V420 H0Z" fill="#fff"/></svg>
  <div class="abs graffiti easy"><span class="small">Easy as</span><span class="big">1, 2, 3</span></div>
  <svg class="abs steps" viewBox="0 0 380 120">
    <circle cx="48" cy="34" r="26" fill="#16295a"/><circle cx="190" cy="34" r="26" fill="#16295a"/><circle cx="332" cy="34" r="26" fill="#16295a"/>
    <text x="48" y="40" fill="#fff" font-family="Montserrat,Arial,sans-serif" font-weight="900" font-size="18" text-anchor="middle">01</text>
    <text x="190" y="40" fill="#fff" font-family="Montserrat,Arial,sans-serif" font-weight="900" font-size="18" text-anchor="middle">02</text>
    <text x="332" y="40" fill="#fff" font-family="Montserrat,Arial,sans-serif" font-weight="900" font-size="18" text-anchor="middle">03</text>
    <path d="M80 34H150M222 34H292" stroke="#1f5fa8" stroke-width="3"/><path d="M150 28l8 6-8 6zM292 28l8 6-8 6z" fill="#1f5fa8"/>
  </svg>
  <div class="step-text" style="left:26px;top:590px">Call us for a free quote</div>
  <div class="step-text" style="left:168px;top:590px">We assess the surface and plan</div>
  <div class="step-text" style="left:310px;top:590px">Graffiti gone, property restored</div>
  <div class="photo truck" role="img" aria-label="White service truck with pressure washing equipment"></div>
  <div class="abs info-box">Beacon Rinse &amp; Spray removes graffiti and washes walls, lots and entrances across the region.</div>
  <div class="abs since">WASHING &amp; STEAMING SERVICES<strong>SINCE 2011</strong></div>
  <p class="copy study">Studies have shown that fast removal is the best way to prevent repeat graffiti and keep a property looking its best.</p>
  <div class="photo before" role="img" aria-label="Concrete wall with graffiti before cleaning"></div>
  <div class="label" style="left:18px;top:1075px;width:184px">BEFORE</div>
  <div class="photo after" role="img" aria-label="Concrete wall clean after graffiti removal"></div>
  <div class="label" style="left:218px;top:1075px;width:184px">AFTER</div>
  <div class="brand"><span class="mark"></span><span class="name">Beacon Rinse<br>&amp; Spray</span></div>
  <p class="abs call">No matter what's seen on your property, we clean it up. <strong>Call Beacon Rinse &amp; Spray.</strong></p>
  <svg class="abs footer" viewBox="0 0 420 130" preserveAspectRatio="none"><path d="M0 20 C140 0 280 0 420 20 V130 H0Z" fill="#16295a"/></svg>
  <div class="contact-phone"><svg width="24" height="24" viewBox="0 0 24 24"><path d="M6.6 10.8a15 15 0 006.6 6.6l2.2-2.2c.3-.3.7-.4 1-.2 1.1.4 2.3.6 3.6.6.6 0 1 .4 1 1V20c0 .6-.4 1-1 1A17 17 0 013 4c0-.6.4-1 1-1h3.5c.6 0 1 .4 1 1 0 1.3.2 2.5.6 3.6.1.3 0 .7-.2 1z" fill="#fff"/></svg>780-555-0143</div>
  <div class="contact-lines">derek@beaconrinse.ca<br>www.beaconrinseandspray.ca</div>
</div>

</body>
</html>
```